Business Card Design

I need a business card that is sleek/professional, I am a hair stylist that is trendy and I want my business cards to fit my style. I would like for them to be black or gray and maybe the print to be white. I also want them to be read easily, I don't want clients to have to squint their eyes to see the print. I want the back of the card to have a space for me to write there next appointment on and maybe a short sentence thanking them for their visit.

Industry/Entity Type

Hair

Contact Information for Business Card

Hair Horizons by Renato @ Gavin Marlow Salons, Owner/Hair Stylist/Makeup Artist-Renato Quillan ,Delmont Method Educator, 4318B Orchard Ridge Dr Ste.262 Sugarland Tx 77512,Phone# 281-555-0193

```html
<!DOCTYPE html>
<html lang="en">
<head>
<meta charset="utf-8">
<title>Hair Horizons by Renato — Business Card</title>
<link rel="stylesheet" href="https://fonts.googleapis.com/css2?family=Fondamento:ital@0;1&family=Didact+Gothic&display=swap">
<style>
  :root {
    --paper: #ffffff;
    --card: #0a0a0a;
    --ink: #ffffff;
    --hair-light: #f4f4f4;
    --hair-dark: #1a1a1a;
  }
  * { margin: 0; padding: 0; box-sizing: border-box; }
  html, body {
    width: 1200px;
    height: 684px;
    overflow: hidden;
    background: var(--paper);
  }
  .canvas {
    position: relative;
    width: 1200px;
    height: 684px;
    background: var(--paper);
  }
  .card {
    position: absolute;
    left: 21px;
    top: 11px;
    width: 1162px;
    height: 661px;
    background: var(--card);
    overflow: hidden;
  }
  .card__title {
    position: absolute;
    left: 30px;
    top: 8px;
    font-family: "Fondamento", "Times New Roman", serif;
    font-size: 168px;
    line-height: 1;
    color: var(--ink);
    white-space: nowrap;
    letter-spacing: 1px;
  }
  .card__thanks {
    position: absolute;
    left: 768px;
    top: 186px;
    font-family: "Fondamento", "Times New Roman", serif;
    font-style: italic;
    font-size: 40px;
    line-height: 1;
    color: var(--ink);
    white-space: nowrap;
  }
  .card__hair-art {
    position: absolute;
    left: 705px;
    top: 235px;
    width: 457px;
    height: 426px;
  }
  .card__contact {
    position: absolute;
    left: 13px;
    top: 525px;
    font-family: "Didact Gothic", "Helvetica", sans-serif;
    font-size: 25px;
    line-height: 35px;
    color: var(--ink);
    white-space: nowrap;
  }
</style>
</head>
<body>
<div class="canvas">
  <section class="card">
    <h1 class="card__title">Hair stylist</h1>
    <p class="card__thanks">thanks for ur visit</p>

    <svg class="card__hair-art" viewBox="0 0 457 426" role="img" aria-label="White silhouette of a tousled, layered hairstyle seen from the side">
      <defs>
        <linearGradient id="hair-tone" x1="0" y1="0" x2="0" y2="1">
          <stop offset="0" stop-color="var(--hair-light)"/>
          <stop offset="0.55" stop-color="var(--hair-light)"/>
          <stop offset="1" stop-color="var(--hair-dark)"/>
        </linearGradient>
      </defs>
      <rect x="0" y="0" width="457" height="426" fill="url(#hair-tone)"/>
    </svg>

    <address class="card__contact">
      Hair Horizons by Renato @ Gavin Marlow Salons,<br>
      Owner/Hair Stylist/Makeup Artist-Renato Quillan ,Delmont<br>
      Method Educator, 4318B Orchard Ridge Dr Ste.262<br>
      Sugarland Tx 77512,Phone# 281-555-0193
    </address>
  </section>
</div>
</body>
</html>
```